Brightwell Power Solutions

We'd like a web design that's beautiful and professional. We replace existing inefficient systems (mostly lighting at the moment but expanding) with highly efficient systems.

```html
<!DOCTYPE html>
<html lang="en">
<head>
<meta charset="utf-8">
<title>Brightwell Power Solutions</title>
<link href="https://fonts.googleapis.com/css2?family=Open+Sans:wght@400;600;700&display=swap" rel="stylesheet">
<style>
:root{
  --green:#0d8f3a;
  --green-text:#1f8f3c;
  --page:#d9d9d9;
  --white:#ffffff;
  --nav:#333333;
  --ink:#555555;
  --ink-dark:#333333;
  --rule:#cfcfcf;
  --panel:#efefef;
  --footer:#3a3a3a;
  --footer-text:#a8a8a8;
  --blue:#1677d2;
}
*{box-sizing:border-box;margin:0;padding:0}
html,body{width:845px;height:1200px;overflow:hidden}
body{font-family:"Open Sans",Arial,sans-serif;background:var(--page);position:relative;color:var(--ink)}
.abs{position:absolute}
.header{left:0;top:0;width:845px;height:80px;background:var(--green)}
.brand{left:58px;top:9px;width:75px;height:62px;background:var(--white);border:1px solid #cfcfcf;display:flex;align-items:center;justify-content:center;gap:4px}
.brand-dot{width:7px;height:7px;background:var(--green)}
.brand-name{font-size:10px;font-weight:600;color:var(--green)}
.contact-line{right:57px;top:16px;font-size:10px;color:var(--white)}
.contact-line b{font-weight:700}
.nav{left:340px;top:50px;width:448px;height:30px;background:var(--nav)}
.nav a,.nav .sep{position:absolute;top:8px;font-size:9px;line-height:12px;color:var(--white);text-decoration:none;white-space:nowrap}
.nav a.current{color:var(--green)}
.search{left:649px;top:55px;width:129px;height:19px;background:var(--white);border:1px solid #bbb}
.search-btn{right:0;top:0;width:21px;height:17px;border-left:1px solid #ccc;display:flex;align-items:center;justify-content:center}
.content{left:58px;top:84px;width:729px;height:972px;background:var(--white)}
.hero{left:58px;top:84px;width:729px;height:290px;background:linear-gradient(180deg,#2a2558 0%,#3c3a6a 35%,#4a4462 60%,#5a4a56 75%,#7b5a6a 88%,#3a3040 100%)}
.hero-title{left:106px;top:217px;font-size:19px;font-weight:700;color:var(--white);letter-spacing:.2px}
.hero-sub{left:106px;top:239px;font-size:12px;color:var(--white)}
.dots{left:382px;top:346px;display:flex;gap:16px}
.dots span{width:9px;height:9px;border-radius:50%;background:rgba(255,255,255,.35)}
.dots span.on{background:var(--green)}
.h-section{font-size:16px;color:var(--green-text);font-weight:400}
.who-title{left:58px;width:729px;top:394px;text-align:center}
.who-text{left:126px;width:593px;top:425px;font-size:9.3px;line-height:11.3px;text-align:center}
.rule{left:94px;width:658px;height:1px;background:var(--rule)}
.products-title{left:58px;width:729px;top:535px;text-align:center;font-size:11.5px;font-weight:400;color:var(--ink-dark);letter-spacing:.3px}
.product{top:570px;width:192px}
.product-img{width:192px;height:128px;border:1px solid #cfcfcf}
.product-name{margin-top:7px;text-align:center;font-size:11.5px;color:var(--ink-dark);letter-spacing:.3px}
.product-link{text-align:center;font-size:7px;color:var(--green-text);letter-spacing:.4px}
.unique-title{left:90px;top:771px}
.unique-list{left:94px;top:806px;width:412px;list-style:none}
.unique-list li{position:relative;padding-left:27px;font-size:9.3px;line-height:11px;margin-bottom:11px;color:var(--ink)}
.unique-list li b{color:var(--ink-dark);font-weight:600}
.unique-list li svg{position:absolute;left:0;top:-1px}
.audit{left:528px;top:774px;width:226px;height:239px;background:var(--panel)}
.audit-head{height:30px;background:var(--green);color:var(--white);font-weight:700;font-size:10.5px;display:flex;align-items:center;justify-content:center}
.field{position:absolute;left:13px;width:200px;height:22px;display:flex;align-items:center;justify-content:space-between;font-size:8.5px;color:var(--ink-dark)}
.field span.input{width:128px;height:22px;background:var(--white);border:1px solid #d4d4d4}
.submit{position:absolute;left:148px;top:194px;width:59px;height:24px;background:var(--blue);color:var(--white);font-size:9px;font-weight:700;display:flex;align-items:center;justify-content:center;border-radius:2px}
.footer{left:0;top:1056px;width:845px;height:144px;background:var(--footer)}
.footer-divider{width:1px;background:#4d4d4d;top:1056px;height:109px}
.footer-bottom-rule{left:0;top:1165px;width:845px;height:1px;background:#4d4d4d}
.f-title{font-size:10.5px;color:var(--green-text);font-weight:600}
.f-text{font-size:7.5px;line-height:9.5px;color:var(--footer-text);text-transform:uppercase}
.f-links{font-size:9px;line-height:11px;color:var(--footer-text)}
.flag{left:522px;top:1072px;width:74px;height:40px;background:linear-gradient(90deg,#6a76a8 0%,#b8aebc 50%,#c76a7e 100%);border-radius:2px}
.tagline{left:612px;top:1091px;font-size:8px;font-weight:400;color:var(--white)}
.socials{left:697px;top:1138px;display:flex;gap:4px}
.socials span{width:16px;height:16px;border-radius:50%;background:#9a9a9a}
.copyright{right:91px;top:1177px;font-size:7.5px;color:#8a8a8a}
</style>
</head>
<body>
<header>
  <div class="abs header"></div>
  <div class="abs brand"><span class="brand-dot"></span><span class="brand-name">Brightwell</span></div>
  <div class="abs contact-line">CONTACT US ON: <b>5550 2147</b></div>
  <nav class="abs nav">
    <a class="current" href="#" style="left:11px">HOME</a><span class="sep" style="left:46px">|</span>
    <a href="#" style="left:58px">WHY LED</a><span class="sep" style="left:106px">|</span>
    <a href="#" style="left:118px">CASE STUDIES</a><span class="sep" style="left:186px">|</span>
    <a href="#" style="left:198px">FAQ</a><span class="sep" style="left:223px">|</span>
    <a href="#" style="left:235px">ENERGY AUDIT</a>
  </nav>
  <div class="abs search">
    <div class="abs search-btn">
      <svg width="12" height="12" viewBox="0 0 12 12"><circle cx="5" cy="5" r="3.6" fill="none" stroke="#555" stroke-width="1.6"/><line x1="7.6" y1="7.6" x2="11" y2="11" stroke="#555" stroke-width="1.8"/></svg>
    </div>
  </div>
</header>

<main>
  <div class="abs content"></div>
  <div class="abs hero" role="img" aria-label="City skyline at night with a cable-stayed bridge and light trails over the river"></div>
  <div class="abs hero-title">LED FOR EVERY APPLICATION</div>
  <div class="abs hero-sub">For Product Details Contact us right now</div>
  <div class="abs dots"><span class="on"></span><span></span><span></span><span></span></div>

  <h2 class="abs h-section who-title">Who We Are</h2>
  <p class="abs who-text">Brightwell Power Solutions is an acknowledged Green Energy leader providing energy saving lighting solutions. Our LEED trained professionals coupled with our close relationships with the leading LED manufacturers around the world, ensures that your LED retrofit project will be affordable; saving you up to 75% on your lighting costs and drastically reducing replacement costs. Our turn-key system takes care of everything from the initial lighting energy audit, to an energy saving solution, to professional installation, and finally complete cleanup and proper disposal.</p>

  <div class="abs rule" style="top:514px"></div>
  <h3 class="abs products-title">PRODUCTS &amp; SERVICES</h3>

  <div class="abs product" style="left:121px">
    <div class="product-img" role="img" aria-label="Two LED replacement bulbs on a white background" style="background:radial-gradient(ellipse at 45% 50%,#c9ddd6 0%,#e8eeec 55%,#ffffff 100%)"></div>
    <div class="product-name">LED LAMPS</div>
    <div class="product-link">VIEW ALL</div>
  </div>
  <div class="abs product" style="left:327px">
    <div class="product-img" role="img" aria-label="Outdoor LED street luminaire" style="background:linear-gradient(135deg,#f2f2f2 0%,#c8c8c8 55%,#9a9a9a 100%)"></div>
    <div class="product-name">OUTDOOR LUMINAIRES</div>
    <div class="product-link">VIEW ALL</div>
  </div>
  <div class="abs product" style="left:533px">
    <div class="product-img" role="img" aria-label="LED work light with coiled cable and power driver" style="background:radial-gradient(ellipse at 55% 50%,#9a9a9a 0%,#d8d8d8 45%,#ffffff 80%)"></div>
    <div class="product-name">LIGHTING ELECTRONICS</div>
    <div class="product-link">VIEW ALL</div>
  </div>

  <div class="abs rule" style="top:754px"></div>

  <h2 class="abs h-section unique-title">Why We Are Unique</h2>
  <ul class="abs unique-list">
    <li><svg width="15" height="15" viewBox="0 0 15 15"><circle cx="7.5" cy="7.5" r="7.5" fill="#0d8f3a"/><circle cx="7.5" cy="7.5" r="4.2" fill="none" stroke="#fff" stroke-width="1"/></svg>Established in 1986 with 25 years of outstanding service, a <b>GSA approved vendor</b></li>
    <li><svg width="15" height="15" viewBox="0 0 15 15"><circle cx="7.5" cy="7.5" r="7.5" fill="#0d8f3a"/><circle cx="7.5" cy="7.5" r="4.2" fill="none" stroke="#fff" stroke-width="1"/></svg>A <b>Service-Disabled Veteran-Owned</b> company focused on hiring Service Disabled Veterans, Veterans and family members of veterans</li>
    <li><svg width="15" height="15" viewBox="0 0 15 15"><circle cx="7.5" cy="7.5" r="7.5" fill="#0d8f3a"/><circle cx="7.5" cy="7.5" r="4.2" fill="none" stroke="#fff" stroke-width="1"/></svg>As a member of the <b>National Green Building Alliance</b>, we support green design, construction and operations</li>
    <li><svg width="15" height="15" viewBox="0 0 15 15"><circle cx="7.5" cy="7.5" r="7.5" fill="#0d8f3a"/><circle cx="7.5" cy="7.5" r="4.2" fill="none" stroke="#fff" stroke-width="1"/></svg><b>LEED</b> (Leadership in Energy &amp; Environmental Design) trained employees</li>
    <li><svg width="15" height="15" viewBox="0 0 15 15"><circle cx="7.5" cy="7.5" r="7.5" fill="#0d8f3a"/><circle cx="7.5" cy="7.5" r="4.2" fill="none" stroke="#fff" stroke-width="1"/></svg><b>DUNS</b> Number - 482913706</li>
    <li><svg width="15" height="15" viewBox="0 0 15 15"><circle cx="7.5" cy="7.5" r="7.5" fill="#0d8f3a"/><circle cx="7.5" cy="7.5" r="4.2" fill="none" stroke="#fff" stroke-width="1"/></svg><b>CAGE</b> Code - 7K3P9</li>
    <li><svg width="15" height="15" viewBox="0 0 15 15"><circle cx="7.5" cy="7.5" r="7.5" fill="#0d8f3a"/><circle cx="7.5" cy="7.5" r="4.2" fill="none" stroke="#fff" stroke-width="1"/></svg>Active in System for Award Management <b>(SAM)</b> - Registration valid until 07/15/2014</li>
    <li><svg width="15" height="15" viewBox="0 0 15 15"><circle cx="7.5" cy="7.5" r="7.5" fill="#0d8f3a"/><circle cx="7.5" cy="7.5" r="4.2" fill="none" stroke="#fff" stroke-width="1"/></svg>Registered <b>NAICS</b> codes - 238210, 335110, 335122</li>
    <li><svg width="15" height="15" viewBox="0 0 15 15"><circle cx="7.5" cy="7.5" r="7.5" fill="#0d8f3a"/><circle cx="7.5" cy="7.5" r="4.2" fill="none" stroke="#fff" stroke-width="1"/></svg>LED products available on <b>GSA Schedule - GS-00F-4821X</b></li>
  </ul>

  <form class="abs audit">
    <div class="audit-head">REQUEST Q FREE AUDIT</div>
    <div class="field" style="top:53px"><span>Your name*:</span><span class="input"></span></div>
    <div class="field" style="top:90px"><span>Company*:</span><span class="input"></span></div>
    <div class="field" style="top:126px"><span>Phone number:</span><span class="input"></span></div>
    <div class="field" style="top:163px"><span>Email Address:</span><span class="input"></span></div>
    <div class="submit">SUBMIT</div>
  </form>
</main>

<footer>
  <div class="abs footer"></div>
  <div class="abs footer-divider" style="left:302px"></div>
  <div class="abs footer-divider" style="left:469px"></div>
  <div class="abs footer-bottom-rule"></div>
  <div class="abs f-title" style="left:91px;top:1070px">CONTACT</div>
  <div class="abs f-text" style="left:91px;top:1093px">Field Office<br>c/o Harbor Trade Center<br>418 Meridian Street<br>20145 Lakeside</div>
  <div class="abs f-title" style="left:344px;top:1070px">LINKS</div>
  <div class="abs f-links" style="left:346px;top:1092px">Home<br>Why LED?<br>Case Studies<br>FAQ<br>Energy Audit</div>
  <div class="abs flag" role="img" aria-label="Photograph of a waving national flag"></div>
  <div class="abs tagline">PROMOTING ENERGY INDEPENDENCE</div>
  <div class="abs socials"><span></span><span></span><span></span></div>
  <div class="abs copyright">© COPYRIGHT 2014 . BRIGHTWELL PRODUCTS INC. | ALL RIGHTS ARE RESERVED</div>
</footer>
</body>
</html>
```